Restaurant needs take out menu design

I need a takeout menu design for a new restaurant. We will be printing via quillpressly.com. On their website, you can download blank templates.

See specs:
1. 11x17 accordion folding. http://www.quillpressly.com/take-out-menu-printing.html
2. Font is Times New Roman
3. All design/font on the menu will be black

*See menu inspiration attached. Feel free to reuse similar boarders and design.
*Attached is our logo
*Please let me know if any other information is needed.
*Attached is a our menu with prices.
*Please send to me in an ai file.

Industry/Entity Type

Restaurant

Font styles to use
Serif
Decorative

Requirements
Must have
• new times roman. black lettering
• all uppercase lettering
• must be in adobe illustrator format
• have the same feel as the menus I attached
Nice to have
• Leave the area for the telephone numbers, hours, address and business hours the same as the copy and pasted menu.
Should not have
• No other color than black

```html
<!DOCTYPE html>
<html lang="en">
<head>
<meta charset="utf-8">
<title>The Jade Terrace – Take Out Menu</title>
<link href="https://fonts.googleapis.com/css2?family=Tinos:wght@400;700&display=swap" rel="stylesheet">
<style>
  :root{
    --backdrop-light:#d8c39a;
    --backdrop-dark:#b89a64;
    --panel:#f8f0de;
    --panel-edge:#efe2c6;
    --ink:#000000;
    --rule:#000000;
    --photo-light:#d9cfc0;
    --photo-dark:#a89a88;
  }
  *{margin:0;padding:0;box-sizing:border-box}
  html,body{width:1200px;height:776px;overflow:hidden}
  body{
    position:relative;
    background:radial-gradient(ellipse at 50% 50%,var(--backdrop-light),var(--backdrop-dark));
    font-family:"Tinos","Times New Roman",serif;
    color:var(--ink);
    text-transform:uppercase;
  }
  .panel{position:absolute;top:19px;height:738px;background:radial-gradient(ellipse at 50% 40%,var(--panel),var(--panel-edge))}
  .panel--left{left:19px;width:271px}
  .panel--middle{left:310px;width:581px}
  .panel--right{left:910px;width:271px}

  .t{position:absolute;white-space:nowrap;line-height:12px}
  .section-title{position:absolute;left:0;width:100%;text-align:center;font-weight:700;font-size:28px;letter-spacing:.5px;line-height:30px}
  .item{font-weight:700;font-size:9.4px}
  .note{font-size:8.4px}
  .price{position:absolute;font-weight:700;font-size:9.4px;text-align:right;line-height:12px}
  .dish{font-size:7.8px}
  .dish-strong{font-weight:700;font-size:8.6px}
  .group-title{font-weight:700;font-size:10.6px;letter-spacing:.4px}
  .tier-price{position:absolute;width:120px;text-align:center;font-weight:700;font-size:15px;line-height:16px}
  .divider{position:absolute;height:1px;background:var(--rule)}
  .chili{position:absolute;width:17px;height:7px}
  .tiny{font-size:5.8px}

  .intro{position:absolute;left:0;width:100%;text-align:center;font-size:8.4px;line-height:12px;white-space:nowrap}
  .intro--strong{font-weight:700}

  .brand-name{position:absolute;left:0;width:100%;text-align:center;font-weight:400;font-size:34px;line-height:38px;letter-spacing:2px}
  .contact{position:absolute;font-size:23px;line-height:26px;white-space:nowrap}
  .hours-title{position:absolute;left:0;width:100%;text-align:center;font-weight:700;font-size:18px;letter-spacing:.5px}
  .hours{position:absolute;right:41px;text-align:right;font-size:12px;line-height:16.4px}
  .web{position:absolute;left:40px;top:697px;font-size:13px;display:flex;align-items:center;gap:5px}
  .photo-band{position:absolute;left:20px;width:231px;height:1px;background:var(--rule)}
</style>
</head>
<body>

<svg width="0" height="0" style="position:absolute" aria-hidden="true">
  <symbol id="chili-mark" viewBox="0 0 20 8">
    <path d="M1 5 C6 2 12 1 17 2 L19 1 L18 3 C14 6 7 7 1 5 Z" fill="var(--ink)"/>
  </symbol>
</svg>

<section class="panel panel--left">
  <h2 class="section-title" style="top:22px">Vegetables</h2>

  <div class="t item" style="left:27px;top:55px">Moo Shu Vegetables</div><div class="price" style="right:11px;top:55px">$11.95</div>
  <div class="t item" style="left:27px;top:73px">Dried Sauteed String Beans</div><div class="price" style="right:11px;top:73px">$11.95</div>
  <svg class="chili" style="left:6px;top:94px"><use href="#chili-mark"/></svg>
  <div class="t item" style="left:27px;top:92px">Sauteed Broccoli in Garlic Sauce</div><div class="price" style="right:11px;top:92px">$11.95</div>
  <div class="t item" style="left:27px;top:110px">Eggplant in Garlic Sauce</div><div class="price" style="right:11px;top:110px">$11.95</div>
  <svg class="chili" style="left:6px;top:130px"><use href="#chili-mark"/></svg>
  <div class="t item" style="left:27px;top:128px">Mixed Vegetables in Brown Sauce</div><div class="price" style="right:11px;top:128px">$11.95</div>
  <div class="t item" style="left:27px;top:147px">Ever Green in Light Fresh Garlic Sauce $11.95</div>
  <div class="t note" style="left:27px;top:160px">(Broccoli, String Beans, Asparagus and Snow Peas)</div>
  <div class="t item" style="left:27px;top:178px">Soft Bean Curd Casserole</div><div class="price" style="right:11px;top:178px">$11.95</div>
  <div class="t item" style="left:27px;top:196px">Sauteed Shanghai Bok Choy</div><div class="price" style="right:11px;top:196px">$11.95</div>
  <div class="t item" style="left:27px;top:214px">Bean Curd with Mixed Vegetables</div><div class="price" style="right:11px;top:214px">$12.75</div>

  <h2 class="section-title" style="top:240px">Side Orders</h2>
  <div class="price" style="right:50px;top:269px">Pt.</div><div class="price" style="right:11px;top:269px">Qt.</div>

  <div class="t item" style="left:27px;top:282px">Pancake</div><div class="price" style="right:50px;top:282px">(1)</div><div class="price" style="right:11px;top:282px">50</div>
  <div class="t item" style="left:27px;top:300px">Fresh Crispy Noodles</div><div class="price" style="right:11px;top:300px">1.50</div>
  <div class="t item" style="left:27px;top:319px">Canned Soda</div><div class="price" style="right:11px;top:319px">1.50</div>
  <div class="t item" style="left:27px;top:337px">White Rice</div><div class="price" style="right:50px;top:337px">1.75</div><div class="price" style="right:11px;top:337px">3.00</div>
  <div class="t item" style="left:27px;top:356px">Brown Rice</div><div class="price" style="right:50px;top:356px">2.25</div><div class="price" style="right:11px;top:356px">4.00</div>
  <div class="t item" style="left:27px;top:374px">Fried Rice</div><div class="price" style="right:50px;top:374px">6.95</div><div class="price" style="right:11px;top:374px">8.95</div>
  <div class="t note" style="left:27px;top:387px;font-size:9.4px">(Chicken, Pork, or Vegetable)</div>
  <div class="t item" style="left:27px;top:406px">Fried Rice <span style="font-weight:400">(Beef or Shrimp)</span></div><div class="price" style="right:50px;top:406px">7.95</div><div class="price" style="right:11px;top:406px">9.95</div>
  <div class="t item" style="left:27px;top:425px">House Special Fried Rice</div><div class="price" style="right:50px;top:425px">8.95</div><div class="price" style="right:11px;top:425px">9.95</div>
  <div class="t note" style="left:27px;top:436px;font-size:7px">Brown Rice Available upon Request</div>
  <div class="t note" style="left:27px;top:447px;font-size:7px">for an Extra Charge $1.00</div>
  <div class="t item" style="left:27px;top:464px">Lo Mein</div><div class="price" style="right:50px;top:464px">7.95</div><div class="price" style="right:11px;top:464px">9.95</div>
  <div class="t note" style="left:27px;top:477px;font-size:9.4px">(Chicken, Pork, or Vegetable)</div>
  <div class="t item" style="left:27px;top:496px">House Special Lo Mein</div><div class="price" style="right:50px;top:496px">10.50</div><div class="price" style="right:11px;top:496px">12.50</div>
  <div class="t item" style="left:27px;top:515px">Chow Mein</div><div class="price" style="right:11px;top:515px">9.95</div>
  <div class="t note" style="left:27px;top:526px">(Chicken, Pork, Beef, Shrimp, Vegetable, or House)</div>
  <div class="t item" style="left:27px;top:544px">Chow Fun Noodles</div><div class="price" style="right:11px;top:544px">9.95</div>
  <div class="t note" style="left:27px;top:557px">(Chicken, Pork, Beef, Shrimp, Vegetable, or House)</div>
  <div class="t item" style="left:27px;top:574px">Mei Fun Noodles</div><div class="price" style="right:11px;top:574px">9.95</div>
  <div class="t note" style="left:27px;top:587px">(Chicken, Pork, Beef, Shrimp, Vegetable, or House)</div>
  <div class="t item" style="left:27px;top:604px">Curry Mei Fun Singapore</div>
  <div class="t item" style="left:27px;top:616px">Style with Egg</div><div class="price" style="right:11px;top:616px">12.95</div>
  <div class="t item" style="left:27px;top:634px">Cantonese Pan Fried Noodles</div><div class="price" style="right:11px;top:634px">16.95</div>
  <div class="t note" style="left:27px;top:647px">(Crispy Egg Noodles with Chicken, Pork, Shrimp,</div>
  <div class="t note" style="left:27px;top:659px">Mushrooms and Vegetables in a Delicate White</div>
  <div class="t note" style="left:27px;top:670px">Sauce)</div>
</section>

<section class="panel panel--middle">
  <h2 class="section-title" style="top:21px">Lunch Specialties</h2>
  <p class="intro intro--strong" style="top:56px">Served from 11:30 am - 3 pm Monday - Friday (Excluding Holiday)</p>
  <p class="intro" style="top:73px">• With a Choice of Soup: Wonton, Egg Drop or <svg class="chili" style="position:relative;left:auto;top:0;width:13px;height:6px"><use href="#chili-mark"/></svg> Hot &amp; Sour Soup or Soda (Except Noodle Soup)</p>
  <p class="intro" style="top:88px">• With a Choice or Rice white Rice, Brown Rice Or Vegetable Fried Rice Egg Roll or Shrimp Roll $2.00 Extra</p>
  <div class="divider" style="left:62px;top:103px;width:460px"></div>

  <div class="tier-price" style="left:78px;top:132px">$ 8.75</div>
  <div class="t group-title" style="left:31px;top:150px">Bean Curd with Mixed Vegetables</div>
  <div class="t group-title" style="left:31px;top:163px">Sauteed Mixed Vegetables</div>
  <svg class="chili" style="left:10px;top:180px"><use href="#chili-mark"/></svg>
  <div class="t dish-strong" style="left:31px;top:178px">Broccoli in Garlic Sauce</div>
  <div class="t dish" style="left:31px;top:191px">Dried Sauteed String Beans Lo Mein With Roast Pork,</div>
  <div class="t dish" style="left:31px;top:204px">Chicken, Beef, Or Shrimp Chow Mein With Roast Pork,</div>
  <div class="t dish" style="left:31px;top:217px">Chicken, Beef, Or Shrimp</div>
  <div class="divider" style="left:85px;top:238px;width:108px"></div>

  <div class="tier-price" style="left:78px;top:248px">$ 8.95</div>
  <div class="t group-title" style="left:31px;top:267px">Chicken, Beef, Pork, or Baby Shrimp</div>
  <div class="t dish" style="left:31px;top:280px">With A Choice Of Broccoli, String Beans,</div>
  <div class="t dish" style="left:31px;top:293px">Or Mixed Vegetables And A Choice</div>
  <div class="t dish" style="left:31px;top:306px">Of Brown Sauce,</div>
  <svg class="chili" style="left:10px;top:324px"><use href="#chili-mark"/></svg>
  <div class="t dish-strong" style="left:31px;top:322px">Garlic Sauce, Black Bean Sauce or</div>
  <div class="t dish-strong" style="left:31px;top:335px">White Sauce</div>
  <div class="t dish" style="left:31px;top:347px">Sweet &amp; Sour Chicken Or Pork Pepper Steak</div>
  <div class="t dish" style="left:31px;top:361px">With Onions</div>
  <svg class="chili" style="left:10px;top:378px"><use href="#chili-mark"/></svg>
  <div class="t dish-strong" style="left:31px;top:376px">Sauteed Shredded Beef with Hot Sauce</div>
  <div class="t dish-strong" style="left:31px;top:389px">Chicken with Cashew Nuts</div>
  <div class="divider" style="left:85px;top:409px;width:108px"></div>

  <div class="tier-price" style="left:78px;top:417px">$10.95</div>
  <div class="t group-title" style="left:31px;top:435px">Jumbo Shrimp with Broccoli</div>
  <div class="t dish" style="left:31px;top:449px">Jumbo Shrimp With Mixed Vegetables</div>
  <div class="t dish" style="left:31px;top:462px">Shrimp With Lobster Sauce</div>
  <svg class="chili" style="left:10px;top:481px"><use href="#chili-mark"/></svg>
  <div class="t dish-strong" style="left:31px;top:479px">Kung Po Shrimp with Peanuts</div>
  <div class="t dish" style="left:31px;top:492px">Sauteed Two Delicacies Scallop With Mixed Vegetables</div>
  <svg class="chili" style="left:10px;top:512px"><use href="#chili-mark"/></svg>
  <div class="t dish-strong" style="left:31px;top:510px">Scallops with Garlic Sauce</div>

  <div class="tier-price" style="left:373px;top:132px">$9.25</div>
  <div class="t group-title" style="left:328px;top:150px">Sesame Chicken</div>
  <svg class="chili" style="left:307px;top:171px"><use href="#chili-mark"/></svg>
  <div class="t dish-strong" style="left:328px;top:169px">General Tso's Chicken</div>
  <svg class="chili" style="left:307px;top:189px"><use href="#chili-mark"/></svg>
  <div class="t dish-strong" style="left:328px;top:187px">Tangerine Chicken</div>
  <div class="t dish" style="left:328px;top:200px">Orange Liqueur Chicken Sesame Beef</div>
  <svg class="chili" style="left:307px;top:220px"><use href="#chili-mark"/></svg>
  <div class="t dish-strong" style="left:328px;top:218px">Tangerine Beef</div>
  <div class="t dish" style="left:328px;top:232px">Peking Pork Chops</div>
  <svg class="chili" style="left:307px;top:254px"><use href="#chili-mark"/></svg>
  <div class="t dish-strong" style="left:328px;top:252px">Mandarin Pork Chops</div>
  <svg class="chili" style="left:307px;top:273px"><use href="#chili-mark"/></svg>
  <div class="t dish-strong" style="left:328px;top:271px">Triple Crown</div>
  <div class="t dish" style="left:328px;top:284px;font-size:7.3px">Pork Chop Noodle Soup Ten Ingredients Noodle Soup</div>
  <div class="t tiny" style="left:328px;top:297px">(Chicken, Pork, Shrimp, And Mixed Vegetables In A Chicken Broth)</div>
  <svg class="chili" style="left:307px;top:317px"><use href="#chili-mark"/></svg>
  <div class="t dish-strong" style="left:328px;top:315px">Beef Noodle Soup</div>
  <svg class="chili" style="left:307px;top:336px"><use href="#chili-mark"/></svg>
  <div class="t dish-strong" style="left:328px;top:334px">Dan Dan Noodles <span style="font-weight:400">(Peanut Sesame Noodles)</span></div>
  <svg class="chili" style="left:307px;top:355px"><use href="#chili-mark"/></svg>
  <div class="t dish-strong" style="left:328px;top:353px;font-size:7.8px">Peking Noodles <span style="font-weight:400">&nbsp;(Minced Pork, Bean Curd, And</span></div>
  <div class="t dish" style="left:328px;top:367px">Bamboo In A Brown Hoisin Sauce)</div>
  <div class="divider" style="left:378px;top:394px;width:109px"></div>

  <div class="tier-price" style="left:373px;top:417px">$11.50</div>
  <div class="t group-title" style="left:328px;top:435px">Crispy Shrimp</div>
  <svg class="chili" style="left:307px;top:455px"><use href="#chili-mark"/></svg>
  <div class="t dish-strong" style="left:328px;top:453px">General Tso's Shrimp</div>
  <svg class="chili" style="left:307px;top:475px"><use href="#chili-mark"/></svg>
  <div class="t dish-strong" style="left:328px;top:473px">Hunan Shrimp with Walnuts</div>
  <div class="t dish" style="left:328px;top:487px">Orange Liqueur Shrimp</div>
  <svg class="chili" style="left:307px;top:510px"><use href="#chili-mark"/></svg>
  <div class="t dish-strong" style="left:328px;top:508px">Seafood Supreme</div>
  <div class="t dish" style="left:328px;top:521px">Happy Family</div>
  <svg class="chili" style="left:307px;top:544px"><use href="#chili-mark"/></svg>
  <div class="t dish-strong" style="left:328px;top:542px">General Tso's Triple Fragrance</div>

  <div style="position:absolute;left:0;width:100%;top:628px;text-align:center;font-size:17px;line-height:20px">
    <svg style="width:17px;height:7px"><use href="#chili-mark"/></svg>Hot &amp; Spicy<svg style="width:17px;height:7px;transform:scaleX(-1)"><use href="#chili-mark"/></svg>
  </div>
  <p class="intro" style="top:652px">We Can Alter The Spiciness Accorsing To Yor Taste</p>
  <p class="intro intro--strong" style="top:665px">Crispy Noodles Only Come With Soup Or Show Mein</p>
  <p class="intro" style="top:690px">Additional Sauce On The Side- Extra Charge $2.00</p>
</section>

<section class="panel panel--right">
  <div class="brand-name" style="top:120px">The Jade Terrace</div>

  <div role="img" aria-label="Chili pepper illustration" style="position:absolute;left:93px;top:229px;width:85px;height:24px;border-radius:50% 40% 50% 50%;background:var(--ink)"></div>

  <div class="divider" style="left:28px;top:283px;width:91px"></div>
  <div class="divider" style="left:143px;top:283px;width:88px"></div>
  <svg style="position:absolute;left:121px;top:273px;width:20px;height:20px" viewBox="0 0 20 20" aria-hidden="true">
    <circle cx="10" cy="10" r="9" fill="none" stroke="var(--ink)" stroke-width="1.2"/>
    <path d="M5.5 8.5 Q10 5 14.5 8.5 L13.5 10 L12 9.3 L12 8.6 Q10 8 8 8.6 L8 9.3 L6.5 10 Z M7.5 10.5 L12.5 10.5 L13.5 13.5 L6.5 13.5 Z" fill="var(--ink)"/>
  </svg>

  <div class="contact" style="left:40px;top:299px">Tel.: (555) 014-2782</div>
  <div class="contact" style="right:34px;top:331px">(555) 019-5355</div>
  <div class="contact" style="left:34px;top:363px">Fax.: (555) 014-2713</div>
  <div class="divider" style="left:34px;top:393px;width:203px"></div>

  <div class="photo-band" style="top:414px"></div>
  <div role="img" aria-label="Photo of a plated rice and chicken dish with a fresh salad and a bowl of sauce" style="position:absolute;left:28px;top:417px;width:227px;height:146px;background:radial-gradient(ellipse at 45% 60%,var(--photo-dark),var(--photo-light))"></div>
  <div class="photo-band" style="top:564px"></div>

  <div class="hours-title" style="top:584px">Business Hours</div>
  <div class="hours" style="top:603px">Mon. Thurs: 11:30 A.M. - 9:30 P.M.<br>Friday: 11:30 A.M. - 10:30 P.M.<br>Saturday: 12:30 P.M. - 10:30 P.M.<br>Sunday: 12:00 Noon - 9:30 P.M.</div>

  <div class="web">
    <svg width="15" height="15" viewBox="0 0 16 16" aria-hidden="true">
      <circle cx="8" cy="8" r="7" fill="none" stroke="var(--ink)" stroke-width="1.2"/>
      <ellipse cx="8" cy="8" rx="3" ry="7" fill="none" stroke="var(--ink)" stroke-width="1"/>
      <path d="M1 8 H15 M2.5 4.5 H13.5 M2.5 11.5 H13.5" stroke="var(--ink)" stroke-width="1"/>
    </svg>
    www.thejadeterrace.com
  </div>
</section>

</body>
</html>
```